"Harbor Pouch" - Envelope Package for 3 Small Pamphlets/Tracts

We need a design for an envelope package that will be folded to fit 3 small tracts/pamphlets. The final product will be paper that is simply folded - not glued or stapled. The tracts/pamphlets themselves are the ones that can be found at www.brimcanada.ca/literature - they don't need to be designed as we already have them in print. We just want a package/envelope to put them in so we can hand them out in a creative way.

We are looking for a few different ideas to choose from - which is why we are coming to you! Attached is a design brief that outlines the desired format and pictures of mocked-finished product. Also attached is the "B" (BRIM logo). One of the pictures will provide you with the final product measurement in millimetres. You will have to add safety margins for full bleed to send to the printer. This needs to be designed in Photoshop or Illustrator. Photoshop is preferred.

Although I like the white background because it looks clean, please also provide a darker background to see if the "wallet" effect would work. (I am talking about the outside of the package. the inside should remain white.)

I like the concept of the icons for body and mind, but the icon for "spirit" should be something like a generic sunrise, sunset or peaceful lake.

You will notice that there are "folding" numbers inside the attached mockup picture. We would like them to be nicely designed on the final product so that people know how to fold the envelope, but those numbers should be hidden behind the flaps/pamphlets once the 3 pamphlets are in and the product is fully folded. We would also like to have light grey dotted lines to know where to fold on the inside of the package.

On the centre back panel is where you have the question that states "Know someone who needs healing?"

```html
<!DOCTYPE html>
<html lang="en">
<head>
<meta charset="utf-8">
<title>Harbor Pouch – Dieline, Inside and Outside</title>
<link rel="stylesheet" href="https://fonts.googleapis.com/css2?family=Arimo:wght@400;700&family=Noto+Serif:ital,wght@0,700;1,400&display=swap">
<style>
  :root {
    --navy: #023363;
    --bleed: #ee1c24;
    --cut: #111111;
    --fold: #a6a6a6;
    --paper: #ffffff;
    --arrow: #8f8f8f;
    --label: #000000;
  }
  html, body {
    margin: 0;
    padding: 0;
    overflow: hidden;
    background: var(--paper);
  }
  .sheet {
    display: block;
    width: 810px;
    height: 1200px;
  }
  .bleed-line { fill: none; stroke: var(--bleed); stroke-width: 1.6; }
  .cut-line { fill: none; stroke: var(--cut); stroke-width: 1.6; }
  .fold-line { fill: none; stroke: var(--fold); stroke-width: 0.8; stroke-dasharray: 4 3; }
  .fold-line--light { stroke: #c8c8c8; }
  .fold-arrow { fill: var(--arrow); }
  .fold-number { font-family: "Arimo", sans-serif; font-size: 6px; fill: #ffffff; }
  .view-label { font-family: "Arimo", sans-serif; font-size: 37px; fill: var(--label); text-anchor: middle; }
  .band { fill: var(--navy); }
  .panel-title { font-family: "Noto Serif", serif; font-style: italic; font-size: 19px; fill: #ffffff; text-anchor: middle; }
  .question { font-family: "Noto Serif", serif; font-style: italic; font-size: 30px; fill: var(--navy); text-anchor: middle; }
  .product-name { font-family: "Noto Serif", serif; font-weight: 700; font-size: 35px; fill: var(--navy); text-anchor: middle; }
  .brand-name { font-family: "Noto Serif", serif; font-weight: 700; font-size: 22px; fill: #ffffff; letter-spacing: 3px; }
  .brand-dot { fill: #ffffff; }
  .icon-frame { stroke: #9a9a9a; stroke-width: 1; }
  .legend { font-family: "Arimo", sans-serif; font-weight: 700; font-size: 37px; }
  .legend--cut { fill: var(--cut); }
  .legend--bleed { fill: var(--bleed); }
  .legend--fold { fill: var(--fold); }
</style>
</head>
<body>
<svg class="sheet" viewBox="0 0 810 1200" xmlns="http://www.w3.org/2000/svg">
  <defs>
    <linearGradient id="tone-runner" x1="0" y1="0" x2="0" y2="1">
      <stop offset="0" stop-color="#6f8fb5"/>
      <stop offset="0.55" stop-color="#f2a23a"/>
      <stop offset="1" stop-color="#3a2a1a"/>
    </linearGradient>
    <linearGradient id="tone-mind" x1="0" y1="0" x2="0" y2="1">
      <stop offset="0" stop-color="#d0305a"/>
      <stop offset="0.5" stop-color="#2a4fa8"/>
      <stop offset="1" stop-color="#0a1d4a"/>
    </linearGradient>
    <radialGradient id="tone-sunrise" cx="0.5" cy="0.55" r="0.6">
      <stop offset="0" stop-color="#fff6c8"/>
      <stop offset="0.45" stop-color="#f6b43c"/>
      <stop offset="1" stop-color="#8c5a6a"/>
    </radialGradient>
    <path id="arrow-shape" d="M0 -4 L7 -4 L7 -9 L16 0 L7 9 L7 4 L2 4 A6 6 0 0 0 2 12 L-2 12 A10 10 0 0 1 0 -4 Z"/>
  </defs>

  <!-- INSIDE VIEW -->
  <g class="inside-view">
    <path class="bleed-line" d="M118.3 50.6 H691.7 V329.1 H739.8 V389 H691.7 V437 H118.3 V389 H70.3 V329.1 H118.3 Z"/>
    <path class="cut-line" d="M130.2 63 H679.8 V341.5 H727.9 V377.1 H679.8 V425.2 H130.2 V377.1 H82.1 V341.5 H130.2 Z"/>
    <g class="fold-lines">
      <line class="fold-line fold-line--light" x1="315.1" y1="63" x2="315.1" y2="425.2"/>
      <line class="fold-line fold-line--light" x1="499.6" y1="63" x2="499.6" y2="425.2"/>
      <line class="fold-line fold-line--light" x1="130.2" y1="110.6" x2="679.8" y2="110.6"/>
      <line class="fold-line fold-line--light" x1="130.2" y1="377.1" x2="679.8" y2="377.1"/>
      <line class="fold-line fold-line--light" x1="130.2" y1="341.5" x2="130.2" y2="377.1"/>
      <line class="fold-line fold-line--light" x1="679.8" y1="341.5" x2="679.8" y2="377.1"/>
    </g>
    <g class="fold-steps">
      <g transform="translate(100 357)"><use class="fold-arrow" href="#arrow-shape"/><text class="fold-number" x="-1" y="11">1</text></g>
      <g transform="translate(712 357) scale(-1 1)"><use class="fold-arrow" href="#arrow-shape"/><text class="fold-number" x="-1" y="11" transform="scale(-1 1)" dx="-2">2</text></g>
      <g transform="translate(405 408) rotate(-90)"><use class="fold-arrow" href="#arrow-shape"/></g>
      <text class="fold-number" x="396" y="408">3</text>
      <g transform="translate(405 76) rotate(90) scale(1 -1)"><use class="fold-arrow" href="#arrow-shape"/></g>
      <text class="fold-number" x="396" y="85">4</text>
      <g transform="translate(596 243) scale(-1 1)"><use class="fold-arrow" href="#arrow-shape"/></g>
      <text class="fold-number" x="589" y="253">5</text>
      <g transform="translate(213 243)"><use class="fold-arrow" href="#arrow-shape"/><text class="fold-number" x="-1" y="11">6</text></g>
    </g>
    <text class="view-label" x="404.5" y="484">INSIDE</text>
  </g>

  <!-- OUTSIDE VIEW -->
  <g class="outside-view">
    <path class="bleed-line" d="M118.3 517.6 H691.7 V796.6 H739.8 V856.5 H691.7 V904.6 H118.3 V856.5 H70.3 V796.6 H118.3 Z"/>

    <rect class="band band--header" x="118.3" y="530" width="573.4" height="47.6"/>
    <g class="panel-titles">
      <text class="panel-title" transform="translate(219.6 548) rotate(180)">Spirit</text>
      <text class="panel-title" transform="translate(402 548) rotate(180)">Mind</text>
      <text class="panel-title" transform="translate(588 548) rotate(180)">Body</text>
    </g>

    <g class="brand-block">
      <rect class="band" x="495" y="602.9" width="196.7" height="58.4"/>
      <circle class="brand-dot" cx="530" cy="632" r="9"/>
      <text class="brand-name" x="550" y="640">BRIM</text>
    </g>

    <g class="back-question">
      <text class="question" x="402" y="633">Know</text>
      <text class="question" x="402" y="665">someone</text>
      <text class="question" x="402" y="696">who</text>
      <text class="question" x="402" y="728">needs</text>
      <text class="question" x="402" y="759">healing?</text>
    </g>

    <g class="front-title">
      <text class="product-name" x="590" y="719">Harbor</text>
      <text class="product-name" x="590" y="761">Pouch</text>
    </g>

    <line x1="130.2" y1="807" x2="679.8" y2="807" stroke="#9a9a9a" stroke-width="1.6"/>
    <rect class="band band--tab" x="82.1" y="808" width="645.8" height="36.6"/>
    <rect class="band band--bottom" x="130.2" y="844.6" width="549.6" height="47.6"/>

    <g class="panel-icons">
      <rect class="icon-frame" x="339" y="790" width="34" height="34" rx="4" fill="url(#tone-runner)" role="img" aria-label="Photo icon: runner against a sunset sky"/>
      <rect class="icon-frame" x="385.4" y="790" width="34" height="34" rx="4" fill="url(#tone-mind)" role="img" aria-label="Photo icon: glowing human brain in blue figure"/>
      <rect class="icon-frame" x="431.9" y="790" width="34" height="34" rx="4" fill="url(#tone-sunrise)" role="img" aria-label="Photo icon: sunrise over the horizon"/>
      <rect class="icon-frame" x="524.4" y="790" width="34" height="34" rx="4" fill="url(#tone-runner)" role="img" aria-label="Photo icon: runner against a sunset sky"/>
      <rect class="icon-frame" x="570.9" y="790" width="34" height="34" rx="4" fill="url(#tone-mind)" role="img" aria-label="Photo icon: glowing human brain in blue figure"/>
      <rect class="icon-frame" x="617.3" y="790" width="34" height="34" rx="4" fill="url(#tone-sunrise)" role="img" aria-label="Photo icon: sunrise over the horizon"/>
      <rect class="icon-frame" x="203" y="852.4" width="34" height="34" rx="4" fill="url(#tone-sunrise)" transform="rotate(180 220 869.4)" role="img" aria-label="Photo icon: sunrise, upside down"/>
      <rect class="icon-frame" x="386" y="852.4" width="34" height="34" rx="4" fill="url(#tone-mind)" transform="rotate(180 403 869.4)" role="img" aria-label="Photo icon: glowing brain, upside down"/>
      <rect class="icon-frame" x="570.3" y="852.4" width="34" height="34" rx="4" fill="url(#tone-runner)" transform="rotate(180 587.3 869.4)" role="img" aria-label="Photo icon: runner at sunset, upside down"/>
    </g>

    <g class="fold-lines">
      <line class="fold-line" x1="310" y1="530" x2="310" y2="892.2"/>
      <line class="fold-line" x1="495" y1="530" x2="495" y2="892.2"/>
      <line class="fold-line" x1="130.2" y1="577.6" x2="679.8" y2="577.6"/>
      <line class="fold-line" x1="130.2" y1="844.6" x2="679.8" y2="844.6"/>
      <line class="fold-line" x1="130.2" y1="808" x2="130.2" y2="844.6"/>
      <line class="fold-line" x1="679.8" y1="808" x2="679.8" y2="844.6"/>
    </g>

    <path class="cut-line" d="M130.2 530 H679.8 V808 H727.9 V844.6 H679.8 V892.2 H130.2 V844.6 H82.1 V808 H130.2 Z"/>
    <text class="view-label" x="404.5" y="952">OUTSIDE</text>
  </g>

  <!-- LEGEND -->
  <g class="legend-block">
    <text class="legend legend--cut" x="199" y="1046">Black Line : Cut Line</text>
    <text class="legend legend--bleed" x="199" y="1092">Rad Line : Bleed Line</text>
    <text class="legend legend--fold" x="199" y="1137">Gray Line : Fold Line</text>
  </g>
</svg>
</body>
</html>
```